Newsletter Banner for email based newsletter

Newsletter banner with Veltrix as the main focus and our other 2 companies Morrow and Clearance Partners, included. 72 dpi and in RGB color mode, the banner should be the same dimensions as the attached example (VeltrixNewsHeader2). I have also attached the Veltrix and other logos. Note as soon as we receive a decent banner we will accept it as the period for this is only 1 day.

```html
<!DOCTYPE html>
<html lang="en">
<head>
<meta charset="utf-8">
<title>Veltrix Newsletter Banner</title>
<link rel="stylesheet" href="https://fonts.googleapis.com/css2?family=Arimo:wght@400;700&display=swap">
<style>
  :root {
    --navy: #1f3a68;
    --grey-text: #8a8f97;
    --orange: #e8892a;
    --orange-light: #f2a650;
    --bg-light: #f4f4f4;
    --bg-mid: #d9d9d9;
    --white: #ffffff;
  }
  html, body { margin: 0; padding: 0; overflow: hidden; }
  .banner {
    position: relative;
    width: 1200px;
    height: 214px;
    overflow: hidden;
    font-family: "Arimo", Arial, sans-serif;
    background: linear-gradient(90deg, #9aa0a6 0%, var(--bg-mid) 35%, #ebebeb 60%, var(--bg-light) 100%);
  }
  .backdrop {
    position: absolute; inset: 0;
    background: radial-gradient(ellipse at 30% 50%, rgba(120,110,100,0.35), rgba(255,255,255,0) 60%);
  }
  .tiles { position: absolute; left: 0; top: 0; width: 640px; height: 214px; }
  .brand {
    position: absolute; left: 850px; top: 14px;
    display: flex; align-items: center; gap: 14px;
  }
  .brand-mark { width: 62px; height: 62px; background: var(--navy); }
  .brand-block { display: flex; flex-direction: column; align-items: flex-end; }
  .brand-name {
    font-weight: 700; font-size: 62px; line-height: 54px;
    color: var(--navy); letter-spacing: 1px;
  }
  .brand-sub { font-size: 22px; color: var(--navy); margin-top: 4px; }
  .company { position: absolute; top: 104px; line-height: 1; }
  .company-top { font-size: 38px; color: var(--navy); letter-spacing: -0.5px; }
  .company-bottom { font-size: 32px; color: var(--grey-text); letter-spacing: -0.5px; }
  .company.clearance { left: 778px; }
  .company.morrow { left: 960px; }
  .ribbon {
    position: absolute; left: 755px; right: 0; bottom: 0; height: 42px;
    background: linear-gradient(90deg, var(--orange-light), var(--orange) 40%);
    display: flex; align-items: center; justify-content: flex-end;
    padding-right: 22px; box-sizing: border-box;
  }
  .ribbon-label { color: var(--white); font-size: 26px; letter-spacing: 2px; }
</style>
</head>
<body>
<div class="banner">
  <div class="backdrop" role="img" aria-label="Faded laboratory scene in the background"></div>

  <svg class="tiles" viewBox="0 0 640 214" xmlns="http://www.w3.org/2000/svg">
    <defs>
      <linearGradient id="sky" x1="0" y1="0" x2="1" y2="1">
        <stop offset="0" stop-color="#7fb4e6"/><stop offset="1" stop-color="#3d7fc4"/>
      </linearGradient>
      <radialGradient id="flame" cx="0.55" cy="0.45" r="0.6">
        <stop offset="0" stop-color="#fff2c8"/><stop offset="0.35" stop-color="#e59a3c"/><stop offset="1" stop-color="#3a2418"/>
      </radialGradient>
      <linearGradient id="device" x1="0" y1="0" x2="1" y2="1">
        <stop offset="0" stop-color="#e4e6e8"/><stop offset="1" stop-color="#a9adb2"/>
      </linearGradient>
    </defs>
    <g role="img" aria-label="Photo of an antenna mast against blue sky">
      <rect x="32" y="35" width="142" height="142" rx="22" transform="rotate(45 103 106)" fill="url(#sky)" stroke="#ffffff" stroke-width="5"/>
    </g>
    <g role="img" aria-label="Photo of a flame test in a laboratory">
      <rect x="246" y="35" width="142" height="142" rx="22" transform="rotate(45 317 106)" fill="url(#flame)" stroke="#ffffff" stroke-width="5"/>
    </g>
    <g role="img" aria-label="Photo of a desk telephone under test">
      <rect x="443" y="35" width="142" height="142" rx="22" transform="rotate(45 514 106)" fill="url(#device)" stroke="#ffffff" stroke-width="5"/>
    </g>
  </svg>

  <div class="brand">
    <div class="brand-mark"></div>
    <div class="brand-block">
      <div class="brand-name">VELTRIX</div>
      <div class="brand-sub">Laboratories</div>
    </div>
  </div>

  <div class="company clearance">
    <div class="company-top">clearance</div>
    <div class="company-bottom">partners</div>
  </div>
  <div class="company morrow">
    <div class="company-top">morrow</div>
    <div class="company-bottom">laboratories</div>
  </div>

  <div class="ribbon"><span class="ribbon-label">NEWSLETTER</span></div>
</div>
</body>
</html>
```